Promotional Poster for Music Achievement Program

I need a vertical 11x17 poster designed for a new program called Tempo Rise Music Achievement Program. The poster will be displayed in the lesson rooms and lobbies of music schools who use this program. The main headline of the flyer should be "Ask your teacher about Tempo Rise" And then the additional text should be "Love your lessons and practice like never before with 10 levels of achievement!" I would like to use the logo on the flyer, which I uploaded here. In terms of artwork/design, I am looking for a fun, but clean feel. The purpose of the program is for students to progress through ten levels of achievement as they climb higher and higher to mastery of their instrument at level 10, so a feel of climbing, leveling up, or advancing would be good. And of course, this is a music program, so any musical artwork involved would make sense. But again - nothing too busy or overwhelming!

Target Market(s)

Parents waiting in the lobby of a music school.

Industry/Entity Type

Promotional

Colors

Designer to choose colors to be used in the design.

Requirements
Must have
• - Tempo Rise logo
• - This headline: Ask your teacher about Tempo Rise
• - This additional text: Love your lessons and practice like never before with 10 levels of achievement!
Nice to have
• In terms of artwork/design, I am looking for a fun, but clean feel. The purpose of the program is for students to progress through ten levels of achievement as they climb higher and higher to mastery of their instrument at level 10, so a feel of climbing, leveling up, or advancing would be good. And of course, this is a music program, so any musical artwork involved would make sense. But again - nothing too busy or overwhelming!
Should not have
• Should not be too busy.

```html
<!DOCTYPE html>
<html lang="en">
<head>
<meta charset="utf-8">
<title>Tempo Rise Music Achievement Program – Poster</title>
<link href="https://fonts.googleapis.com/css2?family=Mulish:wght@700;800;900&family=Old+Standard+TT&family=Alfa+Slab+One&display=swap" rel="stylesheet">
<style>
  :root {
    --page-bg: #e9e9e7;
    --poster-cream: #fbf6ef;
    --peach: #f6cfb4;
    --blush: #f1b9c6;
    --lilac: #d9c3e0;
    --brown: #5a2e12;
    --ink: #1e1a17;
    --orange: #ef7d1f;
    --orange-light: #f7a646;
    --piano-dark: #2a2420;
    --piano-gold: #b08a4a;
  }
  * { margin: 0; padding: 0; box-sizing: border-box; }
  html, body {
    width: 1200px; height: 1200px; overflow: hidden;
    background: var(--page-bg);
  }
  .poster {
    position: absolute;
    left: 240px; top: 42px;
    width: 720px; height: 1116px;
    background:
      radial-gradient(ellipse 60% 40% at 50% 45%, rgba(255,255,255,0.9), rgba(255,255,255,0) 70%),
      radial-gradient(ellipse 45% 30% at 18% 60%, rgba(241,185,198,0.75), rgba(241,185,198,0) 70%),
      radial-gradient(ellipse 40% 30% at 85% 62%, rgba(246,190,160,0.8), rgba(246,190,160,0) 70%),
      radial-gradient(ellipse 30% 20% at 12% 52%, rgba(217,195,224,0.6), rgba(217,195,224,0) 70%),
      linear-gradient(180deg, #fbf0e6 0%, var(--poster-cream) 60%, #fbf7f1 100%);
    overflow: hidden;
  }
  .brand {
    position: absolute;
    top: 108px; left: 0; width: 100%;
    display: flex; justify-content: center; align-items: center; gap: 16px;
  }
  .brand-dot {
    width: 40px; height: 40px; border-radius: 50%;
    background: var(--ink);
  }
  .brand-name {
    font-family: 'Mulish', sans-serif;
    font-weight: 800;
    font-size: 50px;
    color: var(--ink);
    letter-spacing: -0.5px;
  }
  .piano-photo {
    position: absolute;
    left: 105px; top: 210px;
    width: 480px; height: 560px;
    border-radius: 8px;
    background:
      radial-gradient(ellipse 55% 45% at 55% 45%, rgba(60,50,42,0.85), rgba(60,50,42,0.35) 70%, rgba(60,50,42,0) 100%),
      linear-gradient(160deg, rgba(176,138,74,0.35), rgba(42,36,32,0.2));
  }
  .headline-lead {
    position: absolute;
    top: 802px; left: 0; width: 100%;
    text-align: center;
    font-family: 'Mulish', sans-serif;
    font-weight: 800;
    font-size: 43px;
    color: var(--brown);
    letter-spacing: -0.3px;
  }
  .headline-name {
    position: absolute;
    top: 852px; left: 0; width: 100%;
    text-align: center;
    font-family: 'Alfa Slab One', serif;
    font-size: 86px;
    line-height: 1.2;
    letter-spacing: 1px;
    background: linear-gradient(180deg, var(--orange-light) 0%, var(--orange) 70%, #e0661a 100%);
    -webkit-background-clip: text;
    background-clip: text;
    color: transparent;
  }
  .tagline {
    position: absolute;
    top: 1000px; left: 0; width: 100%;
    text-align: center;
    font-family: 'Old Standard TT', serif;
    font-size: 29px;
    line-height: 38px;
    color: var(--ink);
  }
  .tagline .highlight {
    font-family: 'Mulish', sans-serif;
    font-weight: 700;
    color: var(--orange);
  }
</style>
</head>
<body>
  <main class="poster">
    <div class="brand">
      <span class="brand-dot" aria-hidden="true"></span>
      <span class="brand-name">Tempo Rise</span>
    </div>

    <div class="piano-photo" role="img" aria-label="Photograph of a black grand piano with its lid open, standing on a soft watercolour background"></div>

    <h1>
      <span class="headline-lead">Ask your teacher about</span>
      <span class="headline-name">TEMPO RISE</span>
    </h1>

    <p class="tagline">
      Love your lessons and practice like<br>
      never before with <span class="highlight">10 levels</span> of achievement!
    </p>
  </main>
</body>
</html>
```